Hollowbrook Coverage Group Circle of Services Marketing Flyer

Business flyer that describes the services offered by an Employee Benefits insurance agency. Flyer will be distributed to current and prospective clients and should visually be professional, simple and keep to current logo and color scheme. The flyer will be used in various situations to promote Hollowbrook Coverage to prospective clients and also in general marketing to current clients. The objective is to show a busy business owner in the middle that does not have time to worry and deal with the headaches of all of the services listed that Hollowbrook Coverage provides.

Target Market(s)

Small and Large employer groups looking for solutions and to modernize the way they purchase and manage employee benefits.

Industry/Entity Type

Health Insurance

Font styles to use
Sans Serif

Colors
33a6d7
0292cd
85cae6

Requirements
Must have
• In the middle I would like a picture of a businessperson that looks busy and stressed out. The "Circle of Services" should shoot out from there all around.
• The services should be listed as:
• 1) Employee Benefits - Health Insurance, Dental, Vision, Life, Disability, Voluntary Life, Critical Illness, Cancer, Accident
• 2) Payroll Services
• 3) Compliance Services - ACA Compliance, ERISA, 1094/1095 Reporting
• 4) Human Resources and Web Based Benefits Enrollment & Administration Systems
• 5) Personal Planning
Nice to have
• website listed - www.hollowbrookcoverage.example
• Phone Numbers:
• Arkansas 501.555.0173
• Tennessee 901.555.0148
Should not have
• Cartoon figures

```html
<!DOCTYPE html>
<html lang="en">
<head>
<meta charset="utf-8">
<title>Hollowbrook Coverage Group – Circle of Services</title>
<link rel="stylesheet" href="https://fonts.googleapis.com/css2?family=Oswald:wght@500&family=PT+Sans:wght@400;700&display=swap">
<style>
:root{
  --mat:#363938;
  --paper:#ffffff;
  --circle:#0aa7e6;
  --circle-title:#9fdcf7;
  --ink:#ffffff;
  --slate:#56595c;
  --brand-blue:#33a6d7;
  --photo-top:#e1e8ee;
  --photo-mid:#bfc8d0;
  --photo-desk:#eef0f1;
}
*{box-sizing:border-box;margin:0;padding:0}
html,body{width:864px;height:1200px;overflow:hidden;background:var(--mat)}
.flyer{position:absolute;left:77px;top:96px;width:710px;height:1007px;background:var(--paper);overflow:hidden}
.hero-photo{position:absolute;left:0;top:0;width:710px;height:804px;
  background:linear-gradient(180deg,var(--photo-top) 0%,#cdd5dc 45%,var(--photo-mid) 75%,var(--photo-desk) 88%,#e6e8ea 100%)}
.tagline{position:absolute;left:358px;top:36px;font:700 36px/42px "PT Sans",sans-serif;color:var(--slate)}
.service{position:absolute;border-radius:50%;background:var(--circle);display:flex;flex-direction:column;align-items:center;justify-content:center;text-align:center}
.service-title{font:500 34px/38px "Oswald",sans-serif;color:var(--circle-title);text-transform:uppercase;letter-spacing:.5px}
.service-list{margin-top:10px;font:500 19px/29px "Oswald",sans-serif;color:var(--ink);text-transform:uppercase}
.service-list.small{font-size:19px;line-height:29px}
.service-title.solo{font-size:34px;line-height:37px}
.service-title.white{color:var(--ink);font-size:19px;line-height:29px}
.benefits{left:44px;top:39px;width:290px;height:290px}
.compliance{left:437px;top:185px;width:234px;height:234px}
.payroll{left:60px;top:376px;width:160px;height:160px}
.planning{left:119px;top:583px;width:166px;height:166px}
.hr{left:463px;top:502px;width:214px;height:214px}
.brand{position:absolute;left:0;top:825px;width:710px;text-align:center}
.brand-name{font:700 42px/50px "PT Sans",sans-serif;color:var(--slate)}
.brand-name::before{content:"";display:inline-block;width:14px;height:14px;border-radius:50%;background:var(--brand-blue);margin-right:12px;vertical-align:middle}
.web{margin-top:12px;font:700 22px/26px "PT Sans",sans-serif;color:var(--slate)}
.phones{margin-top:4px;font:400 18px/22px "PT Sans",sans-serif;color:var(--brand-blue);word-spacing:2px}
</style>
</head>
<body>
<main class="flyer">
  <div class="hero-photo" role="img" aria-label="Photo of a stressed businessman at a desk holding his head, surrounded by papers, a laptop and a travel mug"></div>

  <h1 class="tagline">Strategy<br>Preparation<br>Implementation</h1>

  <section class="service benefits">
    <h2 class="service-title">Employee<br>Benefits</h2>
    <p class="service-list">• Health Insurance • Dental<br>• Vision • Life • Disability<br>• Voluntary Life • Cancer<br>• Critical Illness<br>• Accident</p>
  </section>

  <section class="service compliance">
    <h2 class="service-title">Compliance<br>Services</h2>
    <p class="service-list small">• ACA Compliance<br>• ERISA • 1094/1095<br>Reporting</p>
  </section>

  <section class="service payroll">
    <h2 class="service-title solo">Payroll<br>Services</h2>
  </section>

  <section class="service planning">
    <h2 class="service-title solo">Personal<br>Planning</h2>
  </section>

  <section class="service hr">
    <h2 class="service-title white">Human Resources<br>and Web Based<br>Benefits Enrollment<br>&amp; Administration<br>Systems</h2>
  </section>

  <footer class="brand">
    <p class="brand-name">Hollowbrook Coverage Group</p>
    <p class="web">visit&nbsp; www.hollowbrookcoverage.example</p>
    <p class="phones">Arkansas 501.555.0173&nbsp;&nbsp; Tennessee 901.555.0148</p>
  </footer>
</main>
</body>
</html>
```